New premium brand of candy

Candy for 18-35 year olds, in the trend of new (healthier) food consumption patterns Innovative tastes (cocktail, etc.) Packaging full of humor, shifted, story telling Candy coming out of the drawers to display on the offices ! These are jelly candies with nice shapes. The product must be visible in the package Ideally it would be necessary to work on a DOY Pack The brands Plumby Sweets and Fudge Otters are competing

Target Market(s)

The same customers as the brand plumbysweets.example

Logo Text

GUMMORA / baseline: wildly gummoric sweet

Requirements
Must have
• The logo (see attachment) A graphic flat From the illustration to define a visible part of the candy Doy pack

```html
<!DOCTYPE html>
<html lang="en">
<head>
<meta charset="utf-8">
<title>Gummora – Premium Sweets Doy Pack</title>
<link rel="stylesheet" href="https://fonts.googleapis.com/css2?family=Alice&family=Gochi+Hand&family=Patrick+Hand&display=swap">
<style>
  :root {
    --backdrop: #ececec;
    --pouch: #ffffff;
    --pouch-edge: #e2e2e2;
    --seal-line: #dcdcdc;
    --ink: #1c1c1c;
    --candy-red: #e8472e;
    --candy-orange: #f59a23;
    --candy-yellow: #f4e23a;
    --candy-green: #8fcf3a;
  }
  * { margin: 0; padding: 0; box-sizing: border-box; }
  html, body {
    width: 1154px;
    height: 1200px;
    overflow: hidden;
    background: var(--backdrop);
  }
  .canvas {
    position: relative;
    width: 1154px;
    height: 1200px;
  }
  .pouch {
    position: absolute;
    left: 297px;
    top: 100px;
    width: 560px;
    height: 1000px;
    background: var(--pouch);
    border: 1px solid var(--pouch-edge);
    border-radius: 14px 14px 6px 6px;
  }
  .seal {
    position: absolute;
    left: 0;
    right: 0;
    height: 0;
    border-top: 2px solid var(--seal-line);
  }
  .seal--top { top: 80px; }
  .seal--zip { top: 112px; }
  .seal--zip-lower { top: 126px; }
  .brand {
    position: absolute;
    left: 0;
    right: 0;
    top: 222px;
    text-align: center;
  }
  .brand__name {
    font-family: "Alice", serif;
    font-size: 84px;
    letter-spacing: 2px;
    line-height: 1;
    color: var(--ink);
  }
  .brand__tagline {
    font-family: "Alice", serif;
    font-size: 15px;
    color: var(--ink);
    margin-top: 8px;
    margin-left: -90px;
  }
  .product-line {
    position: absolute;
    left: 0;
    right: 0;
    top: 352px;
    text-align: center;
    font-family: "Gochi Hand", cursive;
    font-size: 40px;
    color: var(--ink);
  }
  .window {
    position: absolute;
    left: 60px;
    top: 455px;
    width: 450px;
    height: 435px;
  }
  .volume {
    position: absolute;
    left: 0;
    right: 0;
    top: 905px;
    text-align: center;
    font-family: "Patrick Hand", cursive;
    font-size: 22px;
    color: var(--ink);
  }
</style>
</head>
<body>
  <main class="canvas">
    <section class="pouch">
      <div class="seal seal--top"></div>
      <div class="seal seal--zip"></div>
      <div class="seal seal--zip-lower"></div>

      <header class="brand">
        <div class="brand__name">gummora</div>
        <div class="brand__tagline">wildly gummoric sweet</div>
      </header>

      <div class="product-line">Premium Sweets</div>

      <svg class="window" viewBox="0 0 450 435" role="img" aria-label="Heap of colourful sugar-coated jelly candies seen through the clear window">
        <defs>
          <linearGradient id="candy-fill" x1="0" y1="0" x2="1" y2="1">
            <stop offset="0" stop-color="var(--candy-orange)"/>
            <stop offset="0.35" stop-color="var(--candy-red)"/>
            <stop offset="0.65" stop-color="var(--candy-yellow)"/>
            <stop offset="1" stop-color="var(--candy-green)"/>
          </linearGradient>
        </defs>
        <path d="M0 435 L0 230 C10 150 60 90 120 60 C160 40 190 10 220 0 C260 10 300 30 340 70 C400 110 440 170 450 230 L450 435 Z" fill="url(#candy-fill)"/>
        <line x1="0" y1="262" x2="450" y2="262" stroke="#ffffff" stroke-opacity="0.6" stroke-width="2"/>
      </svg>

      <div class="volume">300ml</div>
    </section>
  </main>
</body>
</html>
```